TARPLOAD business card design

TARPLOAD is a manufacturer of skip bags supplying both the domestic and commercial market. We wish to convey core characteristics of strength, professionalism and reliability to our customers. We are after a business card that uses our company colours of black and yellow as well as incorporating our logo. Our customers are predominantly in the construction or hardware industry. It is important the cards are professional as we are a small company wishing to appear larger than we actually are. more info on the company and product available at www.tarpload-example.com.au

Target Market(s)

hardware buyers, contruction company owners

Industry/Entity Type

Construction

Requirements
Must have
• company colours of black and yellow - No other colours or variation of yellow black. our company logo. card design must convey "tough"
• Card design must be landscape
• Details to be included on the card are:
• Name and Tiltle
• Phone number : 1300 41 62 53
• Mobile: 0452 718 903
• Fax: 03 9617 4852
• email: dale.hendry@tarpload-example.com.au
• address: PO Box 517, Kelvindale, VIC,3294
• Text in white when on a black background
Nice to have
• I like the idea of the back of the card being black with lighter circle area in the middle with black logo in the centre. Similar to the attached "iconic" card

```html
<!DOCTYPE html>
<html lang="en">
<head>
<meta charset="utf-8">
<title>TARPLOAD business card</title>
<link rel="stylesheet" href="https://fonts.googleapis.com/css2?family=Oswald:wght@700&family=Roboto:wght@400;700&display=swap">
<style>
  :root {
    --black: #000000;
    --card-black: #050505;
    --glow: #4a4a4a;
    --yellow: #f2c500;
    --white: #ffffff;
    --page: #e9e9e9;
  }
  * { margin: 0; padding: 0; box-sizing: border-box; }
  html, body { width: 1200px; height: 900px; overflow: hidden; }
  body {
    background: var(--page);
    font-family: "Roboto", Arial, sans-serif;
    position: relative;
  }
  .card {
    position: absolute;
    left: 279px;
    width: 642px;
    height: 384px;
    overflow: hidden;
  }
  .card--front {
    top: 42px;
    background: radial-gradient(ellipse 52% 60% at 50% 50%, var(--glow) 0%, #1c1c1c 55%, var(--card-black) 100%);
    display: flex;
    align-items: center;
    justify-content: center;
  }
  .brand {
    display: flex;
    align-items: center;
    gap: 10px;
    font-family: "Oswald", Impact, sans-serif;
    font-weight: 700;
    color: var(--black);
    line-height: 1;
    white-space: nowrap;
  }
  .brand__mark {
    width: 0.5em;
    height: 0.5em;
    background: currentColor;
  }
  .card--front .brand { font-size: 48px; }

  .card--back {
    top: 474px;
    background: var(--card-black);
  }
  .back__panel {
    position: absolute;
    inset: 0;
    width: 100%;
    height: 100%;
  }
  .back__brand {
    position: absolute;
    left: 32px;
    top: 124px;
    font-size: 36px;
  }
  .person {
    position: absolute;
    right: 32px;
    top: 30px;
    text-align: right;
  }
  .person__name {
    color: var(--yellow);
    font-weight: 700;
    font-size: 21px;
    letter-spacing: 0.3px;
  }
  .person__title {
    color: var(--white);
    font-size: 19px;
    margin-top: 2px;
  }
  .contacts {
    position: absolute;
    left: 228px;
    top: 184px;
    list-style: none;
  }
  .contacts__row {
    display: flex;
    align-items: center;
    height: 30px;
    color: var(--white);
    font-size: 17.5px;
  }
  .contacts__label {
    width: 30px;
    height: 19px;
    margin-right: 12px;
    background: var(--yellow);
    color: var(--black);
    font-size: 16px;
    line-height: 19px;
    padding-left: 8px;
  }
</style>
</head>
<body>
  <section class="card card--front" aria-label="Card front">
    <div class="brand"><span class="brand__mark"></span><span class="brand__name">TARPLOAD</span></div>
  </section>

  <section class="card card--back" aria-label="Card back">
    <svg class="back__panel" viewBox="0 0 642 384" preserveAspectRatio="none" aria-hidden="true">
      <polygon points="0,0 168,0 258,384 0,384" fill="var(--yellow)"/>
    </svg>
    <div class="brand back__brand"><span class="brand__name">TARPLOAD</span></div>

    <div class="person">
      <p class="person__name">DALE HENDRY</p>
      <p class="person__title">Managing Director</p>
    </div>

    <ul class="contacts">
      <li class="contacts__row"><span class="contacts__label">p:</span>1300 41 62 53</li>
      <li class="contacts__row"><span class="contacts__label">m:</span>0452 718 903</li>
      <li class="contacts__row"><span class="contacts__label">f:</span>03 9617 4852</li>
      <li class="contacts__row"><span class="contacts__label">e:</span>dale.hendry@tarpload-example.com.au</li>
      <li class="contacts__row"><span class="contacts__label">a:</span>PO Box 517, Kelvindale, VIC, 3294</li>
    </ul>
  </section>
</body>
</html>
```